Packaging Design New Cosmetics Range

Small Establish online Beauty company is expanding it's product range into Serums, Sprays and Creams . We are looking for a new fresh packaging design for this launch.
We only use products that are Organic , Not Tested on Animals and Natural products
We would be interested in viewing a White Design , Black design and a designer choice of colors .
First Products are
Rose Water in 100ml glass bottle with box
and a set of 3 Face Serums Vit C , Retinol and Hyaluronic in 30ml Glass bottle = Box
Scrubs and creams will launch later in Q1 2020 however would like a similar feel across all products
Target Market(s)
SEA / US Markets
Industry/Entity Type
Cosmetics
Colors
Designer to choose colors to be used in the design.
Requirements
Must have
- Space Allocated for Product Use and Bar Codes on Box
Nice to have
- Organic , Not tested on animal Logo's

```html
<!DOCTYPE html>
<html lang="en">
<head>
<meta charset="utf-8">
<title>Rose Water Glass Bottle Label – Black</title>
<link rel="stylesheet" href="https://fonts.googleapis.com/css2?family=Saira+Extra+Condensed:wght@200;300;400&family=Source+Sans+3:wght@400&display=swap">
<style>
  :root {
    --key-line: #00f0f5;
    --brand-green: #1ef06e;
    --rose-red: #e8120c;
    --label-black: #000000;
    --ink-white: #ffffff;
    --guide-ink: #111111;
    --page: #ffffff;
    --pattern-grey: #1a1a1a;
  }
  html, body { margin: 0; padding: 0; overflow: hidden; background: var(--page); }
  .artboard { position: relative; width: 1200px; height: 940px; overflow: hidden; background: var(--page); }

  .sheet-title {
    position: absolute; left: 91px; top: 17px; margin: 0; white-space: nowrap;
    font: 400 34px/1 "Source Sans 3", sans-serif;
    color: var(--key-line); letter-spacing: -0.3px;
  }
  .dimensions { position: absolute; left: 0; top: 0; }
  .dimension-value {
    position: absolute; margin: 0;
    font: 400 40px/1 "Source Sans 3", sans-serif; color: var(--key-line);
  }
  .dimension-value--width { left: 572px; top: 78px; }
  .dimension-value--height { left: 35px; top: 433px; }

  .label {
    position: absolute; left: 144px; top: 181px; width: 1007px; height: 640px;
    background: radial-gradient(ellipse at center, var(--pattern-grey) 0%, var(--label-black) 70%);
  }
  .label__keyline {
    position: absolute; left: 31px; top: 32px; width: 942px; height: 575px;
    border: 1px solid var(--key-line);
  }
  .label__heading {
    position: absolute; margin: 0; white-space: nowrap;
    font: 400 26px/1.25 "Saira Extra Condensed", sans-serif; color: var(--brand-green);
    letter-spacing: 0.3px;
  }
  .label__heading--produced { left: 162px; top: 97px; transform: translateX(-50%); text-align: center; }
  .label__heading--directions { right: 93px; top: 95px; text-align: right; }
  .label__heading--ingredients { right: 106px; top: 410px; text-align: right; }
  .label__heading--storage { left: 72px; top: 525px; text-align: left; }

  .brand { position: absolute; left: 497px; top: 74px; width: 0; display: flex; flex-direction: column; align-items: center; }
  .brand__dot { width: 46px; height: 46px; border-radius: 50%; background: var(--brand-green); margin-bottom: 18px; flex: none; }
  .brand__name { font: 400 50px/1 "Saira Extra Condensed", sans-serif; color: var(--brand-green); white-space: nowrap; }

  .product-name {
    position: absolute; left: 503px; top: 262px; transform: translateX(-50%); margin: 0; white-space: nowrap;
    font: 200 58px/1 "Saira Extra Condensed", sans-serif; color: var(--ink-white); letter-spacing: 3px;
  }
  .rose-image {
    position: absolute; left: 405px; top: 337px; width: 194px; height: 157px; border-radius: 48% 52% 45% 55%;
    background: radial-gradient(circle at 50% 45%, #ff4a3a 0%, var(--rose-red) 45%, #9c0a06 85%, transparent 100%);
  }
  .volume {
    position: absolute; left: 500px; top: 532px; transform: translateX(-50%); margin: 0; white-space: nowrap;
    font: 300 40px/1 "Saira Extra Condensed", sans-serif; color: var(--ink-white);
  }

  .colour-guide__title {
    position: absolute; left: 127px; top: 842px; margin: 0; white-space: nowrap;
    font: 400 20px/1 "Saira Extra Condensed", sans-serif; color: var(--guide-ink);
  }
  .swatch__chip { position: absolute; top: 891px; width: 33px; height: 33px; }
  .swatch__name {
    position: absolute; top: 906px; white-space: nowrap;
    font: 400 20px/1 "Saira Extra Condensed", sans-serif; color: var(--guide-ink);
  }
  .swatch__chip--green { left: 125px; background: var(--brand-green); }
  .swatch__name--green { left: 162px; }
  .swatch__chip--red { left: 338px; background: var(--rose-red); }
  .swatch__name--red { left: 375px; }
  .swatch__chip--black { left: 548px; background: var(--label-black); }
  .swatch__name--black { left: 585px; }
  .swatch__chip--key { left: 908px; background: var(--key-line); }
  .swatch__name--key { left: 956px; }
</style>
</head>
<body>
<main class="artboard">
  <h1 class="sheet-title">ROSE WATER GLASS BOTTLE LABEL- BLACK</h1>

  <svg class="dimensions" width="1200" height="940" aria-hidden="true">
    <g stroke="var(--key-line)" stroke-width="1" fill="var(--key-line)">
      <line x1="175" y1="102" x2="175" y2="155"/>
      <line x1="1119" y1="102" x2="1119" y2="155"/>
      <line x1="176" y1="129" x2="1118" y2="129"/>
      <path d="M176 129 l8 -4 v8 z M1118 129 l-8 -4 v8 z"/>
      <line x1="65" y1="213" x2="117" y2="213"/>
      <line x1="65" y1="790" x2="117" y2="790"/>
      <line x1="91" y1="214" x2="91" y2="789"/>
      <path d="M91 214 l-4 8 h8 z M91 789 l-4 -8 h8 z"/>
    </g>
  </svg>
  <p class="dimension-value dimension-value--width">90</p>
  <p class="dimension-value dimension-value--height">55</p>

  <section class="label" role="img" aria-label="Black label background with a fine grey line pattern of repeating floral rosettes">
    <div class="label__keyline"></div>
    <h2 class="label__heading label__heading--produced">PRODUCED &amp;<br>PACKED BY</h2>
    <h2 class="label__heading label__heading--directions">DIRECTIONS FOR USE</h2>
    <h2 class="label__heading label__heading--ingredients">INGREDIENTS</h2>
    <h2 class="label__heading label__heading--storage">STORAGE INSTRUCTIONS</h2>

    <div class="brand">
      <span class="brand__dot"></span>
      <span class="brand__name">Nolvia</span>
    </div>

    <p class="product-name">ROSE WATER</p>
    <div class="rose-image" role="img" aria-label="Photograph of a single red rose in bloom"></div>
    <p class="volume">100 ml</p>
  </section>

  <section class="colour-guide">
    <p class="colour-guide__title">COLOUR GUIDE</p>
    <span class="swatch__chip swatch__chip--green"></span><span class="swatch__name swatch__name--green">PANTONE 3268 C</span>
    <span class="swatch__chip swatch__chip--red"></span><span class="swatch__name swatch__name--red">PANTONE 485 C</span>
    <span class="swatch__chip swatch__chip--black"></span><span class="swatch__name swatch__name--black">BLACK</span>
    <span class="swatch__chip swatch__chip--key"></span><span class="swatch__name swatch__name--key">KEY LINES</span>
  </section>
</main>
</body>
</html>
```